Website for IT Security Company in Austria with small and medium business customer base

I own a one man IT security company with a customer small to medium business customer base and need a professional looking website that contains the following information:
- Home page: About the company....
- Services: The services that I offer. It would be nice to have icons if possible (e.g Keystone Ledger icon, digital certificate icon, ...) but this is not a must have.
- About me
- Blog: This is not a must have. It would be ok to just link it to an external blog.
- Impressum
- Contact: No form, just telephone number and e-mail address
- Anything else that you think is necessary for a professional appearance
Also I attached the company design. I do have all source files for the logo if required.

Target Market(s)

Small and medium business of all branches located in Austria

Industry/Entity Type

Cyber Security

Coding

Coded - Design and coding required

Number of Pages Required

5+ page

Font styles to use
Serif
Sans Serif
Other font styles liked:
• Bitsumishi, Bankgothic

Colors

Designer to choose only greyscale colors for use in the design.

Requirements
Must have
• The website must be a mobile-first design.
The design should not be too colorful or playful.
The logo should be used as much as possible
Navigation bar with multi drop-down menu for the services that I offer.
Example:
Services
-> Implementations
-> Implementation Service A
-> Implementation Service B
-> Security Audit
-> Audit A
-> Audit B
Maybe you could have service cards that describe the services briefly and on click redirect to the site that describes the service in detail.
End of example
Logo
contact
impressum
services that I offer
about me
about the company
Nice to have
• Icons would be nice (e.g. house for homepage, letter for contact, ...)
Also for the services I offer icons would be nice (Keystone Ledger, digtial certificates, hacking, security auditing)
For the fonts I have only sugested Bitsumishi and Bankgothic as they are part of my logo. No sure if you feel they make sense as part of the website
Should not have
• forms.
I want to the site to be made as easy as possible (HTML5, CSS, javascript/php/.net)
I do not want a wordpress template or suchlike.

```html
<!DOCTYPE html>
<html lang="en">
<head>
<meta charset="utf-8">
<title>Slate Harbor – IT Security</title>
<link rel="stylesheet" href="https://fonts.googleapis.com/css2?family=Audiowide&family=Roboto:wght@300;400;500;700&display=swap">
<style>
:root{
  --navy:#0b0a9e;
  --navy-deep:#08077a;
  --ink:#111;
  --text:#555;
  --muted:#777;
  --white:#fff;
  --line:#e6e6e6;
  --hero-top:#0a63b8;
  --hero-bottom:#0b1a78;
  --dark-band:#1b1f28;
}
*{box-sizing:border-box;margin:0;padding:0}
html,body{width:1200px;height:3459px;overflow:hidden}
body{font-family:'Roboto',sans-serif;color:var(--text);background:var(--white);position:relative}
.display{font-family:'Audiowide',sans-serif;color:var(--ink);letter-spacing:2px}
.rule{width:34px;height:3px;background:var(--navy);margin:0 auto}
a{color:inherit;text-decoration:none}

/* header */
.topbar{position:absolute;top:0;left:0;width:1200px;height:82px;background:var(--white)}
.brand{position:absolute;display:flex;align-items:center;gap:8px;font-weight:700;color:var(--ink);letter-spacing:1px}
.brand-mark{width:14px;height:14px;background:var(--ink)}
.topbar .brand{left:92px;top:30px;font-size:16px}
.socials{position:absolute;right:180px;top:34px;display:flex;gap:20px}
.socials span{width:12px;height:12px;border-radius:50%;background:#9a9a9a;display:block}
.lang{position:absolute;right:96px;top:29px;display:flex;align-items:center;gap:6px}
.lang .flag{width:24px;height:24px;border-radius:50%;background:#c8102e}
.mainnav{position:absolute;top:82px;left:0;width:1200px;height:43px;background:var(--navy)}
.mainnav a{position:absolute;top:13px;transform:translateX(-50%);color:var(--white);font-weight:500;font-size:15px}
.mainnav a.active{color:var(--navy-deep)}

/* hero */
.hero{position:absolute;top:125px;left:0;width:1200px;height:551px;background:radial-gradient(ellipse at 50% 30%,#1a8ad8 0%,var(--hero-top) 35%,var(--hero-bottom) 100%);text-align:center}
.hero h1{font-family:'Audiowide',sans-serif;color:var(--white);font-size:62px;font-weight:400;letter-spacing:4px;padding-top:218px}
.hero p{font-family:'Audiowide',sans-serif;color:var(--white);font-size:26px;letter-spacing:14px;margin-top:14px}

/* about */
.about-photo{position:absolute;left:626px;top:763px;width:485px;height:465px;background:linear-gradient(160deg,#e9e9ea,#c9cbcf 60%,#2a2d38)}
.about-name{position:absolute;left:1060px;top:763px;width:51px;height:465px;background:var(--navy);color:var(--white);writing-mode:vertical-rl;font-weight:500;font-size:24px;letter-spacing:1px;display:flex;align-items:center;padding-top:26px;justify-content:flex-start}
.about-card{position:absolute;left:90px;top:799px;width:578px;height:392px;background:var(--white);box-shadow:0 2px 14px rgba(0,0,0,.12);padding:52px 50px 0 33px}
.about-card h2{font-size:34px;font-weight:400}
.about-card .rule{margin:12px 0 0}
.about-card p{margin-top:44px;font-size:16px;font-weight:300;line-height:31px;text-align:justify}
.btn{display:inline-flex;align-items:center;justify-content:center;height:53px;border-radius:27px;font-weight:500;font-size:16px}
.btn-navy{background:var(--navy);color:var(--white)}
.btn-white{background:var(--white);color:var(--navy)}
.btn-ghost{border:2px solid var(--white);color:var(--white)}
.about-card .btn{width:161px;margin-top:40px}

/* welcome */
.welcome{position:absolute;top:1325px;left:0;width:1200px;text-align:center}
.welcome h2{font-size:36px;font-weight:400}
.welcome .rule{margin-top:14px}
.welcome p{margin-top:23px;font-size:15.5px;line-height:29px;font-weight:300;color:#444}

/* split */
.split{position:absolute;top:1519px;left:0;width:1200px;height:412px;display:flex}
.split-panel{width:600px;height:412px;padding:72px 0 0 93px;color:var(--white)}
.split-left{background:linear-gradient(135deg,#0d0c9a,#1513b0 60%,#0b0a8a)}
.split-right{background:linear-gradient(135deg,#2a3246,#141925 70%,#0d1018);padding-left:66px}
.split h3{font-size:22px;font-weight:500}
.split p{margin-top:20px;font-size:15.5px;font-weight:300;line-height:26px;width:450px;text-align:justify}
.split .btn{width:161px;margin-top:29px}

/* services */
.services{position:absolute;top:2025px;left:0;width:1200px;text-align:center}
.services h2{font-size:36px;font-weight:400}
.services .rule{margin-top:12px}
.cards{position:absolute;top:2122px;left:90px;display:flex;gap:15px}
.card{width:330px;height:389px;background:var(--white);box-shadow:0 1px 8px rgba(0,0,0,.12);padding:6px}
.card-img{width:318px;height:200px}
.card-body{padding:15px 2px 0}
.card h4{font-size:22px;font-weight:500;color:var(--ink)}
.card p{margin-top:10px;font-size:16px;font-weight:300;line-height:28.5px;text-align:justify}
.card a{display:block;margin-top:12px;color:var(--navy);font-weight:500;font-size:16px}

/* contact band */
.touch{position:absolute;top:2620px;left:0;width:1200px;height:422px;background:linear-gradient(180deg,#2b303b,var(--dark-band) 60%,#12151b);text-align:center;color:var(--white)}
.touch h2{color:var(--white);font-size:36px;font-weight:400;padding-top:82px}
.touch .rule{background:var(--white);margin-top:14px}
.touch p{width:950px;margin:28px auto 0;font-size:16px;font-weight:300;line-height:29px}
.touch .actions{margin-top:30px;display:flex;justify-content:center;gap:10px}
.touch .btn{width:161px}

/* footer */
.footer{position:absolute;top:3042px;left:0;width:1200px;height:417px}
.footer .brand{left:92px;top:155px;font-size:22px}
.footer .brand .brand-mark{width:20px;height:20px}
.fcol{position:absolute;top:103px}
.fcol h5{font-size:20px;font-weight:500;color:var(--ink);margin-bottom:17px}
.fcol li{list-style:none;font-size:13.5px;color:#444;height:29px;display:flex;align-items:center;gap:14px}
.fcol li i{width:9px;height:9px;background:#999;border-radius:50%;display:inline-block}
.fcol li.plain{padding-left:23px}
.legal{position:absolute;top:357px;width:1200px;text-align:center;font-size:13px;color:#444}
.copy{position:absolute;top:381px;width:1200px;text-align:center;font-size:13.5px;color:#444}
.code{position:absolute;right:30px;top:381px;font-size:13px;color:#666}
</style>
</head>
<body>

<header class="topbar">
  <div class="brand"><span class="brand-mark"></span>SLATE HARBOR</div>
  <div class="socials"><span></span><span></span><span></span><span></span><span></span></div>
  <div class="lang"><span class="flag"></span><svg width="10" height="6" viewBox="0 0 10 6"><path d="M1 1l4 4 4-4" fill="none" stroke="#999" stroke-width="1.5"/></svg></div>
</header>
<nav class="mainnav">
  <a class="active" style="left:263px">Home</a>
  <a style="left:381px">Blog</a>
  <a style="left:513px">About me</a>
  <a style="left:659px">Services</a>
  <a style="left:799px">Contact</a>
  <a style="left:933px">imprint</a>
</nav>

<section class="hero" role="img" aria-label="Blue glowing network of connected particles">
  <h1>SLATE HARBOR</h1>
  <p>IT SECURITY</p>
</section>

<section>
  <div class="about-photo" role="img" aria-label="Portrait photo of the company owner"></div>
  <div class="about-name">LUKAS BRENNER-WEISS</div>
  <div class="about-card">
    <h2 class="display">ABOUT ME</h2>
    <div class="rule"></div>
    <p>In my almost 20 years of experience as an IT administrator, trainer, consultant and solution architect, I was able to work for many companies in different industries and sizes.</p>
    <a class="btn btn-navy">Read More</a>
  </div>
</section>

<section class="welcome">
  <h2 class="display">WELCOME TO SLATE HARBOR!</h2>
  <div class="rule"></div>
  <p>Cyber security incidents are unfortunately no longer a rarity , but rather commonplace.<br>In many cases, increasing IT security could be quite easy.<br>I am happy to support you with my profound practice and years of experience.</p>
</section>

<section class="split">
  <div class="split-panel split-left" role="img" aria-label="Blue tinted photo of monitors with code">
    <h3>Why Slate Harbor?</h3>
    <p>In the best case scenario, IT security should cost as few of your valuable resources as possible. With my help, you do not have to lift a heavy oak shield in the figurative sense, but only use a much lighter but just as hard one made of carbon. So you can continue to put your strength into your work.</p>
    <a class="btn btn-white">Read More</a>
  </div>
  <div class="split-panel split-right" role="img" aria-label="Dark photo of a security operations room with screens">
    <h3>Analyze and optimize</h3>
    <p>pursue the approach of the best possible protection with the greatest possible productivity. For this purpose, I largely use the functionalities that you have with the products you have already purchased.&nbsp; This creates an optimal balance between effective protection and financial outlay.</p>
    <a class="btn btn-navy">Contact Us</a>
  </div>
</section>

<section class="services">
  <h2 class="display">SERVICES</h2>
  <div class="rule"></div>
</section>
<div class="cards">
  <article class="card">
    <div class="card-img" role="img" aria-label="Photo of a developer working at multiple monitors" style="background:linear-gradient(135deg,#3a4350,#6b5a48 60%,#2b2f36)"></div>
    <div class="card-body"><h4>Implementations</h4><p>Lorem ipsum dolor sit amet, consectetur adipiscing elit, sed do eiusmod tempor incididunt ut labore et dolore</p><a>Read More</a></div>
  </article>
  <article class="card">
    <div class="card-img" role="img" aria-label="Photo of a laptop showing a security screen" style="background:linear-gradient(135deg,#1f252e,#4a5563 55%,#20262e)"></div>
    <div class="card-body"><h4>Security check</h4><p>Lorem ipsum dolor sit amet, consectetur adipiscing elit, sed do eiusmod tempor incididunt ut labore et dolore</p><a>Read More</a></div>
  </article>
  <article class="card">
    <div class="card-img" role="img" aria-label="Photo of an engineer in a server room" style="background:linear-gradient(135deg,#2c3a40,#5e7478 50%,#1c2429)"></div>
    <div class="card-body"><h4>Security optimization</h4><p>Lorem ipsum dolor sit amet, consectetur adipiscing elit, sed do eiusmod tempor incididunt ut labore et dolore</p><a>Read More</a></div>
  </article>
</div>

<section class="touch" role="img" aria-label="Dark photo of a person overlooking a city">
  <h2>GET IN TOUCH</h2>
  <div class="rule"></div>
  <p>Lorem ipsum dolor sit amet, consectetur adipiscing elit, sed do eiusmod tempor incididunt ut labore et dolore magna aliqua. Ut enim ad minim veniam, quis nostrud exercitation ullamco laboris nisi ut aliquip ex ea commodo consequat. Duis aute irure dolor in reprehenderit in voluptate velit esse cillum dolore eu fugiat nulla pariatur</p>
  <div class="actions"><a class="btn btn-white">Read More</a><a class="btn btn-ghost">Contact Us</a></div>
</section>

<footer class="footer">
  <div class="brand"><span class="brand-mark"></span>SLATE HARBOR</div>
  <div class="fcol" style="left:496px"><h5>Quick Links</h5><ul>
    <li>Home</li><li>Blog</li><li>About me</li><li>Services</li><li>Contact</li></ul></div>
  <div class="fcol" style="left:742px"><h5>Find Us</h5><ul>
    <li><svg width="9" height="11" viewBox="0 0 9 11"><path d="M4.5 0a4 4 0 0 0-4 4c0 3 4 7 4 7s4-4 4-7a4 4 0 0 0-4-4z" fill="#999"/></svg>Lindenweg 14</li>
    <li class="plain">Graz - 8010</li><li class="plain">Austria</li>
    <li><svg width="11" height="8" viewBox="0 0 11 8"><rect width="11" height="8" fill="#999"/><path d="M0 0l5.5 4L11 0" stroke="#fff" fill="none"/></svg>office@slateharbor.example</li>
    <li><svg width="10" height="10" viewBox="0 0 10 10"><path d="M2 0l2 2.5-1 1.5a6 6 0 0 0 3 3l1.5-1L10 8 8.5 10C4 10 0 6 0 1.5z" fill="#999"/></svg>+43 660 1234567</li></ul></div>
  <div class="fcol" style="left:1015px"><h5>Follow Us</h5><ul>
    <li><i></i>Facenote</li><li><i></i>Snapgram</li><li><i></i>Chirper</li><li><i></i>WorkLink</li><li><i></i>ClipTube</li></ul></div>
  <div class="legal">Legal Notice &nbsp;|&nbsp; Privacy Policy &nbsp;|&nbsp; Cookies Information</div>
  <div class="copy">Copyright © 2021 slateharbor.example. All rights reserved. imprint</div>
  <div class="code">C28</div>
</footer>

</body>
</html>
```